Online Dating Website called WinkAtWheel.net

PLEASE CAN ALL PARTICIPATING DESIGNERS PLEASE SUBMIT ALL PAGES AS DETAILED IN THE ORIGINAL BRIEF BELOW WITHIN 48 HOURS TO AVOID WINKATWHEEL EXTENDING THE CONTEST FURTHER.

We have an online dating website that is 95% fully functional and now require an exciting and creative designer to help us create the best dating experience. We are looking for your ideas on a couple of our key pages. These are our landing, profile and search page. We already have a homepage that we are happy with and winning designers will look to build upon the foundations of the homepage and extend them through their designs.

The premise of the site is the idea that if you've ever seen someone out driving and wished you could communicate because you found them attractive, how would you? Well with WinkAtWheel.net you can. Just enter their vehicle registration number (license plate) in to the website in order to get in touch, flirt and develop a relationship. It also allows users to find each other based on other criteria. It acts as both a specialist service and a normal dating website.

The pages that require developing are 1) our landing page, this is the page users see when they first login to the site, it comprises various pieces of information but it's primary function is a live feed of events generated based on the users favourited profiles and interactions with the user. 2) The profile page is the page where users can edit their own information, given the nature of this page we are looking for a creative design that gives this page some flair. 3) Finally we are looking for ideas for our search page, this page needs to provide a list of users who meet the user's search requirements and display the profile of a selected user.
Updates

Project Deadline Extended
Reason: We've asked for certain pages in our brief to be designed and this still hasn't been done. We've contacted the designers that have currently submitted designs and requested this several times. We still await for this to happen.

Target Market(s)

Male or Female age 18+

Industry/Entity Type

Dating

Requirements
Must have
• Our must have feature is a designer with an open mind. The functionality of the site must be present, all we ask is for you to be creative with the layout. Think out side of the box, change the colours, the layout, and the background as you feel. Make it look current and appealing to the user.
Nice to have
• Theme's carried through from the home page
Should not have
• Do not include Comic Sans or Times New Roman font in your designs.

```html
<!DOCTYPE html>
<html lang="en">
<head>
<meta charset="utf-8">
<title>WinkAtWheel.net – Home</title>
<link rel="stylesheet" href="https://fonts.googleapis.com/css2?family=Arimo:wght@400;700&family=Open+Sans:wght@400&family=Merriweather:wght@700&display=swap">
<style>
  :root{
    --pink:#ff0a7f;
    --blue:#3aa3e6;
    --blue-light:#7fcdf7;
    --green:#7bc41a;
    --green-light:#b8e84a;
    --red:#e82b12;
    --red-light:#ff6a3a;
    --panel:#efefef;
    --panel-edge:#ffffff;
    --text:#222222;
    --muted:#444444;
    --date:#2b3a66;
    --like:#7cc23a;
    --header-top:#3a3a3c;
    --header-bottom:#121214;
  }
  *{box-sizing:border-box;margin:0;padding:0}
  html,body{width:1200px;height:1112px;overflow:hidden}
  body{
    position:relative;
    font-family:"Arimo",Arial,sans-serif;
    color:var(--text);
    background:
      radial-gradient(ellipse 420px 300px at 600px 620px,#d9ff7a 0%,rgba(160,230,40,.6) 35%,rgba(0,0,0,0) 75%),
      radial-gradient(ellipse 700px 520px at 620px 560px,#6fc414 0%,#3f8a0a 45%,#173a05 80%,#0c1f03 100%);
  }

  .site-header{
    position:absolute;left:0;top:0;width:1200px;height:106px;
    background:linear-gradient(var(--header-top),var(--header-bottom));
    border-bottom:1px solid #000;
  }
  .brand{position:absolute;left:65px;top:26px;display:flex;align-items:center;gap:10px}
  .brand-name{font-family:"Open Sans",Arial,sans-serif;font-size:36px;color:#fff;letter-spacing:-.5px}
  .brand-dot{width:26px;height:26px;border-radius:50%;background:var(--pink)}
  .main-nav{position:absolute;top:43px;left:0;width:1200px;font-size:17px}
  .main-nav a{position:absolute;color:#fff;text-decoration:none}
  .main-nav a.active{color:var(--pink)}

  .panel{
    position:absolute;background:var(--panel);
    border:4px solid var(--panel-edge);
    box-shadow:0 0 8px rgba(0,0,0,.35);
  }
  .bar{
    position:absolute;height:37px;border-radius:3px;
    display:flex;align-items:center;justify-content:center;
    font-size:19px;letter-spacing:.5px;color:#0c2a44;
  }
  .bar-blue{background:linear-gradient(var(--blue-light),var(--blue));}
  .bar-green{background:linear-gradient(var(--green-light),var(--green));color:#1f3d05}
  .btn{
    position:absolute;display:flex;align-items:center;justify-content:center;gap:8px;
    color:#fff;font-size:15px;border-radius:2px;
  }
  .btn-blue{background:linear-gradient(#5fb8f2,var(--blue))}
  .btn-red{background:linear-gradient(var(--red-light),var(--red))}
  .btn-green{background:linear-gradient(var(--green-light),var(--green))}
  .field{
    position:absolute;height:31px;background:#fff;border:1px solid #cfcfcf;
    font-size:14px;color:#555;padding:7px 8px;
  }
  .select{display:flex;justify-content:space-between;align-items:center;padding-right:3px}
  .select-arrow{width:20px;height:20px;border:1px solid #888;background:#eee;display:flex;align-items:center;justify-content:center}

  .profile-art{position:absolute;left:23px;top:20px;width:226px;height:159px;border:2px solid #999;
    background:linear-gradient(160deg,#f3efb6 0%,#e9d98a 45%,#9ccf6a 100%)}
  .profile-name{position:absolute;left:0;width:270px;top:196px;text-align:center;color:var(--pink);font-weight:700;font-size:21px}
  .profile-meta{position:absolute;left:0;width:270px;top:224px;text-align:center;font-size:15px;color:#111}

  .stats{position:absolute;left:20px;top:68px;width:232px;font-size:14px;color:var(--muted)}
  .stat-group{border-bottom:1px solid #d5d5d5;padding-bottom:10px;margin-bottom:14px}
  .stat-head{display:flex;justify-content:space-between;font-weight:700;font-size:16px;color:#222;margin-bottom:10px}
  .stat-row{display:flex;justify-content:space-between;line-height:20.5px}

  .feed-item{width:528px;height:211px;left:351px}
  .feed-title{position:absolute;left:6px;top:4px;width:508px;height:39px;background:var(--pink);
    color:#fff;font-weight:700;font-size:19px;padding:9px 15px}
  .feed-photo{position:absolute;left:9px;top:56px;width:98px;height:82px;border:3px solid #fff;box-shadow:0 0 3px rgba(0,0,0,.4);
    background:linear-gradient(150deg,#7c4a2a 0%,#c98660 45%,#e8b493 70%,#8aa06a 100%)}
  .feed-text{position:absolute;left:120px;top:58px;width:390px;font-size:14px;line-height:21px;color:#222}
  .feed-date{position:absolute;left:9px;top:146px;font-size:14px;color:var(--date)}
  .feed-like{position:absolute;left:9px;top:170px;font-size:13px;color:var(--like);display:flex;align-items:center;gap:5px}

  .welcome{left:892px;top:152px;width:276px;height:242px;overflow:hidden;background:#fff}
  .welcome-curve{position:absolute;left:0;top:0}
  .welcome-text{position:absolute;left:56px;top:30px;width:212px;text-align:center;
    font-family:"Merriweather",Georgia,serif;font-size:25px;line-height:34px;color:#333}
  .welcome-text em{font-style:normal;color:var(--pink)}

  .match-list{position:absolute;left:10px;top:54px;width:250px;list-style:none;font-size:13.5px;color:#333}
  .match-list li{display:flex;gap:8px;line-height:17px;margin-bottom:10.7px}
  .match-list b{color:var(--pink)}
  .match-icon{flex:0 0 14px;margin-top:2px}
  .match-grid{position:absolute;left:10px;top:24px}
  .match-card{position:absolute;width:114px;text-align:center;font-weight:700;font-size:15px}
  .match-thumb{width:114px;height:98px;border:3px solid #fff;box-shadow:0 0 3px rgba(0,0,0,.5);margin-bottom:10px}
</style>
</head>
<body>

<header class="site-header">
  <div class="brand"><span class="brand-name">winkatwheel</span><span class="brand-dot"></span></div>
  <nav class="main-nav">
    <a class="active" style="left:475px">Home</a>
    <a style="left:564px">Profile</a>
    <a style="left:654px">Messages</a>
    <a style="left:772px">Matches</a>
    <a style="left:878px">Search</a>
    <a style="left:974px">Support</a>
    <a style="left:1080px">My Account</a>
  </nav>
</header>

<section class="panel" style="left:60px;top:152px;width:278px;height:343px">
  <div class="profile-art" role="img" aria-label="Member profile picture"></div>
  <div class="profile-name">SAM CARTER</div>
  <div class="profile-meta">24 YEARS OLD, MILLBROOK</div>
  <div class="field" style="left:13px;top:259px;width:142px">How Are You?</div>
  <div class="btn btn-blue" style="left:165px;top:259px;width:93px;height:31px">Update</div>
  <div class="btn btn-red" style="left:13px;top:300px;width:117px;height:33px">
    <svg width="14" height="16" viewBox="0 0 14 16"><circle cx="7" cy="4" r="4" fill="#fff"/><path d="M0 16c0-6 3-7 7-7s7 1 7 7z" fill="#fff"/></svg>Profile</div>
  <div class="btn btn-green" style="left:139px;top:300px;width:119px;height:33px">
    <svg width="18" height="14" viewBox="0 0 18 14"><rect x="0" y="3" width="18" height="11" rx="2" fill="#fff"/><rect x="6" y="0" width="6" height="4" fill="#fff"/><circle cx="9" cy="8.5" r="3" fill="#8bd12a"/></svg>Upload</div>
</section>

<section class="panel" style="left:60px;top:519px;width:278px;height:190px">
  <div class="bar bar-green" style="left:13px;top:8px;width:245px">SEEN SOMEONE?</div>
  <div class="field" style="left:13px;top:55px;width:142px;font-size:13px">Search Registration</div>
  <div class="btn btn-blue" style="left:165px;top:55px;width:93px;height:31px">Search</div>
  <div class="field select" style="left:13px;top:96px;width:142px">Make<span class="select-arrow"><svg width="8" height="6"><path d="M0 0h8L4 6z" fill="#222"/></svg></span></div>
  <div class="field select" style="left:13px;top:138px;width:142px">Color<span class="select-arrow"><svg width="8" height="6"><path d="M0 0h8L4 6z" fill="#222"/></svg></span></div>
  <div class="btn btn-red" style="left:165px;top:94px;width:93px;height:77px;flex-direction:column;gap:2px">
    <svg width="36" height="36" viewBox="0 0 36 36"><circle cx="21" cy="14" r="10" fill="none" stroke="#fff" stroke-width="4"/><path d="M14 21L4 32" stroke="#fff" stroke-width="6" stroke-linecap="round"/></svg>Search</div>
</section>

<section class="panel" style="left:60px;top:728px;width:278px;height:400px">
  <div class="bar bar-blue" style="left:13px;top:11px;width:245px">YOUR STATS</div>
  <div class="stats">
    <div class="stat-group">
      <div class="stat-head"><span>LIKES</span><span>124</span></div>
      <div class="stat-row"><span>Images you have liked</span><span>32</span></div>
      <div class="stat-row"><span>Statuses you have liked</span><span>67</span></div>
      <div class="stat-row"><span>Likes on your images</span><span>20</span></div>
      <div class="stat-row"><span>Likes on your statuses</span><span>55</span></div>
    </div>
    <div class="stat-group">
      <div class="stat-head"><span>MESSAGES</span><span>171</span></div>
      <div class="stat-row"><span>Sent messages</span><span>66</span></div>
      <div class="stat-row"><span>Received Messages</span><span>105</span></div>
    </div>
    <div class="stat-group" style="border:0">
      <div class="stat-head"><span>FAVOURITES</span><span>20</span></div>
      <div class="stat-row"><span>Your favourites</span><span>12</span></div>
      <div class="stat-row"><span>Favourited by</span><span>8</span></div>
    </div>
  </div>
</section>

<main>
  <article class="panel feed-item" style="top:152px">
    <h2 class="feed-title">Lady changed her status</h2>
    <div class="feed-photo" role="img" aria-label="Member photo"></div>
    <p class="feed-text">Lorem ipsum dolor sit amet, consectetur adipiscing elit. Maecenas fermentum ante id pellentesque consequat.</p>
    <div class="feed-date">TuesDay 22:37</div>
    <div class="feed-like"><svg width="11" height="10" viewBox="0 0 12 11"><path d="M6 11L1 6A3 3 0 0 1 6 2a3 3 0 0 1 5 4z" fill="#7cc23a"/></svg>Like</div>
  </article>
  <article class="panel feed-item" style="top:371px">
    <h2 class="feed-title">Lady changed her status</h2>
    <div class="feed-photo" role="img" aria-label="Member photo"></div>
    <p class="feed-text">Lorem ipsum dolor sit amet, consectetur adipiscing elit. Maecenas fermentum ante id pellentesque consequat.</p>
    <div class="feed-date">TuesDay 22:37</div>
    <div class="feed-like"><svg width="11" height="10" viewBox="0 0 12 11"><path d="M6 11L1 6A3 3 0 0 1 6 2a3 3 0 0 1 5 4z" fill="#7cc23a"/></svg>Like</div>
  </article>
  <article class="panel feed-item" style="top:590px">
    <h2 class="feed-title">Lady changed her status</h2>
    <div class="feed-photo" role="img" aria-label="Member photo"></div>
    <p class="feed-text">Lorem ipsum dolor sit amet, consectetur adipiscing elit. Maecenas fermentum ante id pellentesque consequat.</p>
    <div class="feed-date">TuesDay 22:37</div>
    <div class="feed-like"><svg width="11" height="10" viewBox="0 0 12 11"><path d="M6 11L1 6A3 3 0 0 1 6 2a3 3 0 0 1 5 4z" fill="#7cc23a"/></svg>Like</div>
  </article>
  <article class="panel feed-item" style="top:808px">
    <h2 class="feed-title">Lady changed her status</h2>
    <div class="feed-photo" role="img" aria-label="Member photo"></div>
    <p class="feed-text">Lorem ipsum dolor sit amet, consectetur adipiscing elit. Maecenas fermentum ante id pellentesque consequat.</p>
    <div class="feed-date">TuesDay 22:37</div>
    <div class="feed-like"><svg width="11" height="10" viewBox="0 0 12 11"><path d="M6 11L1 6A3 3 0 0 1 6 2a3 3 0 0 1 5 4z" fill="#7cc23a"/></svg>Like</div>
  </article>
  <article class="panel feed-item" style="top:1027px">
    <h2 class="feed-title">Lady changed her status</h2>
    <div class="feed-photo" role="img" aria-label="Member photo"></div>
    <p class="feed-text">Lorem ipsum dolor sit amet, consectetur adipiscing elit. Maecenas fermentum ante id pellentesque consequat.</p>
  </article>
</main>

<aside>
  <section class="panel welcome">
    <svg class="welcome-curve" width="268" height="234" viewBox="0 0 268 234">
      <defs><linearGradient id="welcomeBlue" x1="0" y1="0" x2="1" y2="1"><stop offset="0" stop-color="#1d78c4"/><stop offset="1" stop-color="#0a4f96"/></linearGradient></defs>
      <path d="M0 0H268V6C110 4 42 30 40 234H0Z" fill="url(#welcomeBlue)"/>
      <path d="M40 234C42 30 110 4 268 6" fill="none" stroke="#bfe4fb" stroke-width="5"/>
    </svg>
    <p class="welcome-text">Welcome,<br>our site is<br>currently <em>FREE</em><br>during beta<br>testing</p>
  </section>

  <section class="panel" style="left:892px;top:410px;width:276px;height:358px">
    <div class="bar bar-blue" style="left:9px;top:14px;width:247px">YOUR MATCHES</div>
    <ul class="match-list">
      <li><svg class="match-icon" width="14" height="12" viewBox="0 0 14 12"><rect y="2" width="14" height="10" rx="2" fill="#ff0a7f"/><circle cx="7" cy="7" r="2.5" fill="#fff"/></svg><span><b>MIA</b> has uploaded a new image</span></li>
      <li><svg class="match-icon" width="14" height="12" viewBox="0 0 14 12"><rect y="2" width="14" height="10" rx="2" fill="#ff0a7f"/><circle cx="7" cy="7" r="2.5" fill="#fff"/></svg><span><b>MIA</b> has uploaded a new image</span></li>
      <li><svg class="match-icon" width="14" height="12" viewBox="0 0 14 12"><rect y="2" width="14" height="10" rx="2" fill="#ff0a7f"/><circle cx="7" cy="7" r="2.5" fill="#fff"/></svg><span><b>LEE</b> has uploaded a new image</span></li>
      <li><svg class="match-icon" width="14" height="12" viewBox="0 0 14 12"><path d="M7 0C3 0 0 2.5 0 5.5c0 2 1 3 2 4L1 12l4-2c.6.1 1.3.2 2 .2 4 0 7-2.5 7-5S11 0 7 0z" fill="#ff0a7f"/></svg><span><b>MIA</b> has uploaded a new image</span></li>
      <li><svg class="match-icon" width="14" height="12" viewBox="0 0 14 12"><path d="M7 0C3 0 0 2.5 0 5.5c0 2 1 3 2 4L1 12l4-2c.6.1 1.3.2 2 .2 4 0 7-2.5 7-5S11 0 7 0z" fill="#ff0a7f"/></svg><span><b>MIA</b> has uploaded a new image</span></li>
      <li><svg class="match-icon" width="14" height="12" viewBox="0 0 14 12"><path d="M7 0C3 0 0 2.5 0 5.5c0 2 1 3 2 4L1 12l4-2c.6.1 1.3.2 2 .2 4 0 7-2.5 7-5S11 0 7 0z" fill="#ff0a7f"/></svg><span><b>Lee</b> has uploaded a new image</span></li>
      <li><svg class="match-icon" width="14" height="12" viewBox="0 0 14 12"><rect y="2" width="14" height="10" rx="2" fill="#ff0a7f"/><circle cx="7" cy="7" r="2.5" fill="#fff"/></svg><span><b>Robin22</b> has uploaded a new image</span></li>
      <li><svg class="match-icon" width="14" height="12" viewBox="0 0 14 12"><rect y="2" width="14" height="10" rx="2" fill="#ff0a7f"/><circle cx="7" cy="7" r="2.5" fill="#fff"/></svg><span><b>Rangi</b> has uploaded a new image</span></li>
      <li><svg class="match-icon" width="14" height="12" viewBox="0 0 14 12"><rect y="2" width="14" height="10" rx="2" fill="#ff0a7f"/><circle cx="7" cy="7" r="2.5" fill="#fff"/></svg><span><b>LADY</b> has updated her status</span></li>
    </ul>
  </section>

  <section class="panel" style="left:892px;top:768px;width:276px;height:323px">
    <div class="match-grid">
      <div class="match-card" style="left:0;top:0"><div class="match-thumb" role="img" aria-label="Match photo" style="background:linear-gradient(150deg,#6b4a2a,#d39a74 55%,#8fae6a)"></div>MIA</div>
      <div class="match-card" style="left:132px;top:0"><div class="match-thumb" role="img" aria-label="Match photo" style="background:linear-gradient(160deg,#c9d9e8,#7a8f6a 60%,#3c4a2e)"></div>Jack</div>
      <div class="match-card" style="left:0;top:145px"><div class="match-thumb" role="img" aria-label="Match photo" style="background:linear-gradient(160deg,#6fb8e8,#f2c89a 55%,#e98fb6)"></div>Rangi</div>
      <div class="match-card" style="left:132px;top:145px"><div class="match-thumb" role="img" aria-label="Match photo" style="background:linear-gradient(160deg,#5fb7e0,#d667b8 55%,#f0d070)"></div>Frank</div>
    </div>
  </section>
</aside>

</body>
</html>
```